Business Card for By Karel Voss

Looking to have a business card designed for my lifestyle and fitness company. My company offers personal training, online programming and nutrition advice based out of London, United Kingdom.

I'd like to see modern, sleek designs, focusing on black, matte black or matte grey. Design doesn't need to be overly descriptive as this will also be used as a personal business card. I've included my logo.

Please note that my company is no longer called "Fitness by Karel Voss" but instead "By Karel Voss", this is because of my other ventures. Therefore please don't use the "fitness by karel voss" text.

information about my company can be found at www.bykarelvoss.com

Company is also based out of London (United Kingdom) & Sydney (Australia) this could be reflected on the card.

Industry/Entity Type

Business

Contact Information for Business Card

Karel Voss
+44 7382 615027
karel@bykarelvoss.com
www.bykarelvoss.com

Font styles to use
Sans Serif

Requirements
Must have
• All contact details and inclusion of my logo.

```html
<!DOCTYPE html>
<html lang="en">
<head>
<meta charset="utf-8">
<title>By Karel Voss — Business Card</title>
<link href="https://fonts.googleapis.com/css2?family=Lato:wght@400;700;900&display=swap" rel="stylesheet">
<style>
  :root {
    --backdrop: #9a9a9a;
    --card-light: #ffffff;
    --card-dark: #1e1c1d;
    --ink: #1a1a1a;
    --ink-soft: #2b2b2b;
    --paper-text: #ffffff;
    --ghost-light: #ececec;
    --ghost-dark: #262425;
    --shadow: rgba(0,0,0,0.35);
  }
  html, body {
    margin: 0;
    padding: 0;
    width: 1200px;
    height: 900px;
    overflow: hidden;
    background: var(--backdrop);
    font-family: "Lato", Arial, sans-serif;
  }
  .stage { position: relative; width: 1200px; height: 900px; }
  .card {
    position: absolute;
    top: 306px;
    width: 440px;
    height: 272px;
    overflow: hidden;
    box-shadow: 2px 3px 5px var(--shadow);
  }
  .card--front { left: 149px; background: var(--card-light); color: var(--ink); }
  .card--back { left: 608px; background: var(--card-dark); color: var(--paper-text); }

  .ghost-mark {
    position: absolute;
    border-radius: 50%;
  }
  .card--front .ghost-mark { left: 340px; top: 40px; width: 230px; height: 230px; background: var(--ghost-light); }
  .card--back .ghost-mark { left: -130px; top: 20px; width: 230px; height: 230px; background: var(--ghost-dark); }

  .brand {
    position: absolute;
    display: flex;
    align-items: center;
    gap: 12px;
    font-weight: 900;
    text-transform: uppercase;
    letter-spacing: 0.5px;
    white-space: nowrap;
  }
  .brand__dot { border-radius: 50%; background: currentColor; flex: none; }
  .card--front .brand { left: 36px; top: 40px; font-size: 24px; color: var(--ink); }
  .card--front .brand__dot { width: 58px; height: 58px; }
  .card--back .brand {
    left: 0; right: 0; top: 58px;
    flex-direction: column; gap: 16px;
    font-size: 24px; color: var(--paper-text);
  }
  .card--back .brand__dot { width: 70px; height: 70px; }

  .holder {
    position: absolute;
    left: 36px;
    top: 166px;
    margin: 0;
    font-size: 14px;
    font-weight: 900;
    letter-spacing: 0.6px;
    text-transform: uppercase;
  }
  .contact {
    position: absolute;
    left: 36px;
    top: 199px;
    margin: 0;
    padding: 0;
    list-style: none;
    font-size: 12.5px;
    line-height: 16px;
    color: var(--ink-soft);
  }
  .contact li { display: flex; align-items: center; gap: 4px; }
  .contact svg { width: 9px; height: 9px; fill: var(--ink-soft); flex: none; }
</style>
</head>
<body>
<main class="stage">
  <section class="card card--front" aria-label="Card front">
    <div class="ghost-mark" aria-hidden="true"></div>
    <div class="brand"><span class="brand__dot"></span>By Karel Voss</div>
    <h1 class="holder">Karel Voss</h1>
    <ul class="contact">
      <li><svg viewBox="0 0 10 10" aria-hidden="true"><path d="M1 3.5C1 2 2 1 3.2 1h3.6C8 1 9 2 9 3.5V4H6.8V3H3.2v1H1z M2 5h6l1 4H1z"/></svg>+44 7382 615027</li>
      <li><svg viewBox="0 0 10 10" aria-hidden="true"><path d="M0 2h10v6H0z M0 2l5 3.5L10 2" stroke="#fff" stroke-width="0.8"/></svg>karel@bykarelvoss.com</li>
      <li><svg viewBox="0 0 10 10" aria-hidden="true"><circle cx="5" cy="5" r="4.5"/></svg>www.bykarelvoss.com</li>
    </ul>
  </section>

  <section class="card card--back" aria-label="Card back">
    <div class="ghost-mark" aria-hidden="true"></div>
    <div class="brand"><span class="brand__dot"></span>By Karel Voss</div>
  </section>
</main>
</body>
</html>
```